Lantern Hill Publicity is a new boutique Press Office with a small roster of well-chosen clients across an array of disciplines; from Art and Technology to Restaurants and Fashion. Based in Greenpoint Brooklyn, Lantern Hill Publicity achieves outstanding results through hard work, tenacity, efficiency and a sense of humor. We need a simple, versatile and classic design. We would like each side of the card to be white text on a black background.

Boutique

```html
<!DOCTYPE html>
<html lang="en">
<head>
<meta charset="utf-8">
<title>Lantern Hill Publicity — Business Card</title>
<link href="https://fonts.googleapis.com/css2?family=Cinzel:wght@500&family=Montserrat:wght@300;400&display=swap" rel="stylesheet">
<style>
  :root {
    --backdrop: #2b2b2b;
    --card: #0b0b0b;
    --ink: #ffffff;
    --ink-soft: #d9d9d9;
  }
  * { margin: 0; padding: 0; box-sizing: border-box; }
  html, body { width: 1200px; height: 900px; overflow: hidden; }
  body {
    background: var(--backdrop);
    display: flex;
    align-items: center;
    justify-content: center;
    gap: 80px;
  }
  .card {
    width: 440px;
    height: 440px;
    background: var(--card);
    border-radius: 30px;
    position: relative;
    overflow: hidden;
    color: var(--ink);
  }
  /* Contact side */
  .card-back .brand-band {
    position: absolute;
    left: 0; top: 0; bottom: 0;
    width: 120px;
    display: flex;
    align-items: center;
    justify-content: center;
  }
  .card-back .brand-band span {
    writing-mode: vertical-rl;
    transform: rotate(180deg);
    font-family: "Cinzel", serif;
    font-weight: 500;
    font-size: 30px;
    letter-spacing: 3px;
    color: var(--ink);
    white-space: nowrap;
  }
  .contact {
    position: absolute;
    left: 150px; top: 110px; right: 30px;
    font-family: "Montserrat", sans-serif;
    font-weight: 300;
    color: var(--ink-soft);
  }
  .contact .person-name { font-size: 19px; font-weight: 400; color: var(--ink); letter-spacing: 0.5px; }
  .contact .person-title { font-size: 12px; margin-top: 4px; }
  .contact .address { font-size: 12px; line-height: 1.55; margin-top: 26px; }
  .contact ul { list-style: none; margin-top: 8px; font-size: 12px; }
  .contact li { display: flex; align-items: center; gap: 10px; line-height: 1.9; }
  .contact svg { width: 12px; height: 12px; fill: none; stroke: var(--ink); stroke-width: 2; }
  /* Brand side */
  .card-front {
    display: flex;
    align-items: center;
    justify-content: center;
  }
  .card-front .brand-name {
    font-family: "Cinzel", serif;
    font-weight: 500;
    font-size: 34px;
    letter-spacing: 3px;
    line-height: 1.25;
    text-align: center;
    color: var(--ink);
  }
</style>
</head>
<body>
  <section class="card card-back">
    <div class="brand-band"><span>Lantern Hill Publicity</span></div>
    <div class="contact">
      <p class="person-name">DANA MERROW</p>
      <p class="person-title">Title</p>
      <p class="address">Fernleaf, 412 Calder Avenue,<br>Suite #3-20, Brooklyn, NY 11222</p>
      <ul>
        <li><svg viewBox="0 0 24 24"><path d="M5 3h4l2 5-3 2a11 11 0 0 0 6 6l2-3 5 2v4a2 2 0 0 1-2 2A17 17 0 0 1 3 5a2 2 0 0 1 2-2z"/></svg>(555) 214-0386</li>
        <li><svg viewBox="0 0 24 24"><path d="M22 2 11 13M22 2l-7 20-4-9-9-4z"/></svg>info@lanternhill.com</li>
        <li><svg viewBox="0 0 24 24"><circle cx="12" cy="12" r="10"/><path d="M2 12h20M12 2a15 15 0 0 1 0 20M12 2a15 15 0 0 0 0 20"/></svg>www.lanternhill.com</li>
      </ul>
    </div>
  </section>
  <section class="card card-front">
    <p class="brand-name">Lantern Hill<br>Publicity</p>
  </section>
</body>
</html>
```